Real Estate Business Cards

Looking for a clean, sharp and professional look for our Real Estate investment Fund that invests in Multi Family Apartment buildings.

Target Market(s)

Real Estate Fund

Industry/Entity Type

Real Estate

Contact Information for Business Card

Company Description: Real Estate Investment Fund
Company Name: RKW Holdings
Name: Marcus Olvane
Cell: (917) 482-0657
Email: marcus@rkwholdings-example.com
Website: www.rkwholdings-example.com
Address: 418, 9th Street, Brooklyn NY 11218

Colors

Designer to choose colors to be used in the design.

Requirements
Nice to have
• Colors to match logo

```html
<!DOCTYPE html>
<html lang="en">
<head>
<meta charset="utf-8">
<title>RKW Holdings — Business Card</title>
<link href="https://fonts.googleapis.com/css2?family=Alfa+Slab+One&family=Open+Sans:wght@400;600&display=swap" rel="stylesheet">
<style>
  :root {
    --page: #f4f4f6;
    --card: #121628;
    --band: #232437;
    --brand-blue: #1f7ab5;
    --text-blue: #4ea6d4;
    --shadow: rgba(10, 12, 25, 0.25);
  }
  * { margin: 0; padding: 0; box-sizing: border-box; }
  html, body {
    width: 1200px; height: 1200px; overflow: hidden;
    background: var(--page);
  }
  .sheet {
    width: 1200px; height: 1200px;
    display: flex; flex-direction: column; align-items: center; justify-content: center;
    gap: 40px;
  }
  .card {
    position: relative;
    width: 820px; height: 532px;
    background: var(--card);
    border-radius: 40px;
    overflow: hidden;
    box-shadow: 0 8px 24px var(--shadow);
    font-family: "Open Sans", sans-serif;
  }
  .wordmark {
    display: flex; align-items: center; gap: 16px;
    font-family: "Open Sans", sans-serif;
    font-weight: 600;
    color: var(--brand-blue);
    white-space: nowrap;
  }
  .wordmark-square {
    background: var(--brand-blue);
    flex: none;
  }
  /* back side */
  .card-back .wordmark {
    position: absolute; left: 50%; top: 50%;
    transform: translate(-50%, -50%);
    font-size: 50px; letter-spacing: 2px;
  }
  .card-back .wordmark-square { width: 44px; height: 44px; }

  /* front side */
  .card-front .wordmark {
    position: absolute; left: 48px; top: 150px;
    font-size: 32px; letter-spacing: 1px;
  }
  .card-front .wordmark-square { width: 30px; height: 30px; }
  .decor-block {
    position: absolute; left: 0; top: 232px;
    width: 360px; height: 300px;
    background: var(--band);
  }
  .holder {
    position: absolute; left: 373px; top: 196px;
    color: var(--text-blue);
  }
  .holder-name {
    font-family: "Alfa Slab One", serif;
    font-size: 37px; line-height: 1.1; letter-spacing: 0.5px;
  }
  .holder-role {
    font-size: 24px; margin-top: 6px;
  }
  .contacts {
    position: absolute; left: 373px; top: 330px;
    list-style: none; color: var(--text-blue);
    font-size: 23px;
  }
  .contact {
    display: flex; align-items: center; gap: 14px;
    height: 44px;
  }
  .contact-icon {
    width: 24px; height: 24px; flex: none;
    fill: none; stroke: var(--text-blue); stroke-width: 2;
  }
</style>
</head>
<body>
<main class="sheet">

  <section class="card card-back" aria-label="Card back">
    <div class="wordmark"><span class="wordmark-square"></span>RKW Holdings</div>
  </section>

  <section class="card card-front" aria-label="Card front">
    <div class="wordmark"><span class="wordmark-square"></span>RKW Holdings</div>
    <div class="decor-block" role="img" aria-label="Large faint brand mark decoration"></div>

    <div class="holder">
      <h1 class="holder-name">Marcus Olvane</h1>
      <p class="holder-role">Real Estate Investment Fund</p>
    </div>

    <ul class="contacts">
      <li class="contact">
        <svg class="contact-icon" viewBox="0 0 24 24" aria-hidden="true">
          <path d="M6 3l4 4-2 3c1 2.5 3.5 5 6 6l3-2 4 4-3 3C10 21 3 14 3 6z"/>
        </svg>
        (917) 482-0657
      </li>
      <li class="contact">
        <svg class="contact-icon" viewBox="0 0 24 24" aria-hidden="true">
          <rect x="2" y="5" width="20" height="14"/>
          <path d="M2 5l10 8 10-8"/>
        </svg>
        marcus@rkwholdings-example.com
      </li>
      <li class="contact">
        <svg class="contact-icon" viewBox="0 0 24 24" aria-hidden="true">
          <circle cx="12" cy="12" r="10"/>
          <ellipse cx="12" cy="12" rx="4.5" ry="10"/>
          <path d="M2 12h20M4 7h16M4 17h16"/>
        </svg>
        www.rkwholdings-example.com
      </li>
      <li class="contact">
        <svg class="contact-icon" viewBox="0 0 24 24" aria-hidden="true">
          <path d="M12 22s-7-8-7-13a7 7 0 0 1 14 0c0 5-7 13-7 13z" fill="var(--text-blue)" stroke="none"/>
          <circle cx="12" cy="9" r="2.5" fill="var(--card)" stroke="none"/>
        </svg>
        418, 9th Street, Brooklyn NY 11218
      </li>
    </ul>
  </section>

</main>
</body>
</html>
```